website design Investment Fund

I am looking for a custom website that will work on desktop computer, tablet device and a cellular device. I have attached the booklet so you can get an idea of the look we are going for. Would like to use the website eventually for crowdfunding. We like the ski racer and mountain climbing designs.

Target Market(s)

Financial Services

Industry/Entity Type

Financial Service

Coding

Coded - Design and coding required

Number of Pages Required

5+ page

Font styles to use
Sans Serif

Requirements
Must have
• Must be viewable on a cell phone and tablet and desktop
Nice to have
• Contact us form

```html
<!DOCTYPE html>
<html lang="en">
<head>
<meta charset="utf-8">
<title>Norvale Partners</title>
<link rel="stylesheet" href="https://fonts.googleapis.com/css2?family=Oswald:wght@500;600&family=Open+Sans:wght@400;600;700&display=swap">
<style>
:root{
  --blue:#1b4f9f;
  --red:#e32526;
  --ink:#1d1d1d;
  --grey:#8a8f98;
  --line:#cfd3d8;
  --white:#ffffff;
}
*{box-sizing:border-box;margin:0;padding:0}
html,body{width:1200px;height:3088px;overflow:hidden}
body{position:relative;font-family:"Open Sans",Arial,sans-serif;color:var(--ink);background:var(--white)}
.abs{position:absolute}
.heading{font-family:"Oswald",Arial,sans-serif;font-weight:600;color:var(--blue);line-height:1}
.tagline{font-weight:700;color:var(--red);font-size:19px;letter-spacing:.3px}
.btn{position:absolute;background:var(--red);color:var(--white);font-size:14px;display:flex;align-items:center;justify-content:center;border-radius:3px}
.social{display:flex;gap:10px}
.social span{width:27px;height:27px;border-radius:50%;background:var(--white);display:block}

/* top bar */
.topbar{left:0;top:0;width:1200px;height:49px;background:var(--blue)}
.topbar .contact{left:99px;top:14px;color:var(--white);font-size:14px;display:flex;align-items:center;gap:8px}
.topbar .social{position:absolute;right:98px;top:11px}

/* hero */
.hero-bg{left:0;top:49px;width:1200px;height:491px;background:linear-gradient(100deg,#d9d3c6 0%,#cfc6b3 45%,#bba68a 62%,#6d4f39 78%,#5a402f 100%)}
.nav{left:648px;top:49px;width:552px;height:43px;background:var(--red);clip-path:polygon(0 0,100% 0,100% 100%,11% 100%);display:flex;align-items:center;padding-left:34px}
.nav a{color:var(--white);text-decoration:none;font-size:14px;padding:0 19px}
.nav a.active{background:#b61c1d;align-self:stretch;display:flex;align-items:center;padding:0 20px}
.wordmark{position:absolute;display:flex;align-items:center;gap:10px;font-family:"Open Sans",Arial,sans-serif;font-weight:600;font-size:28px}
.wordmark .mark{width:20px;height:20px;border-radius:50%;background:currentColor}
.wordmark.hero-mark{left:99px;top:150px;color:var(--blue)}
.wordmark.foot-mark{left:99px;top:2966px;color:var(--white)}
.hero-title{left:97px;top:228px;font-family:"Oswald",Arial,sans-serif;font-weight:600;font-size:70px;line-height:68px;color:var(--blue)}
.hero-title .red{color:var(--red);display:block}
.hero-text{left:99px;top:378px;width:425px;font-size:13.5px;line-height:22px}
.dots{left:577px;top:471px;display:flex;gap:7px}
.dots span{width:11px;height:11px;border-radius:50%;background:var(--blue)}
.dots span.on{background:var(--red)}

/* about */
.frame{left:144px;top:671px;width:384px;height:329px;border:2px solid var(--red)}
.photo{position:absolute}
.about-title{left:613px;top:672px;font-size:40px}
.about-tag{left:614px;top:719px}
.about-text{left:613px;top:769px;width:490px;font-size:13.5px;line-height:22px}

/* services */
.services-bg{left:0;top:1133px;width:1200px;height:620px;background:linear-gradient(180deg,#cfd3d8 0%,#e4e7ea 30%,#eceef0 70%,#dfe2e5 100%)}
.center{left:0;width:1200px;text-align:center}
.services-title{top:1193px;font-size:40px}
.services-tag{top:1247px}
.svc{position:absolute;width:470px;height:96px}
.svc .icon{position:absolute;left:0;top:0;width:96px;height:96px;border-radius:50%;background:var(--white)}
.svc h3{position:absolute;left:120px;top:12px;font-size:17.5px;font-weight:700;color:#111;white-space:nowrap}
.svc p{position:absolute;left:120px;top:40px;width:330px;font-size:13.5px;line-height:22px}
.svc p em{font-style:normal;color:var(--red)}

/* members */
.members-title{top:1815px;font-size:40px}
.members-tag{top:1874px}
.card{position:absolute;top:1953px;width:230px;height:268px;border:1px solid var(--line);overflow:hidden}
.card .pic{position:absolute;inset:0}
.card .cap{position:absolute;left:0;bottom:0;width:100%;height:60px;background:rgba(20,20,20,.85);text-align:center}
.card .cap b{display:block;color:var(--red);font-size:18px;font-weight:700;margin-top:6px}
.card .cap span{display:block;color:var(--white);font-size:13.5px;margin-top:2px}

/* contact */
.contact-bg{left:0;top:2308px;width:1200px;height:545px;background:linear-gradient(90deg,#b9c2cc 0%,#d3d8de 30%,#eef0f2 55%,#f6f7f8 100%)}
.contact-title{left:611px;top:2385px;font-size:37px}
.contact-tag{left:613px;top:2436px;width:500px;line-height:22px}
.field{position:absolute;height:36px;border:1px solid var(--line);background:var(--white);font-size:13.5px;color:var(--grey);padding:10px 16px}

/* footer */
.footer-bg{left:0;top:2853px;width:1200px;height:190px;background:linear-gradient(180deg,#101f35 0%,#0b1627 100%)}
.fnav{right:98px;top:2938px;display:flex;gap:21px;font-size:14px;color:var(--white)}
.fnav .active{color:var(--red)}
.finfo{right:98px;top:2975px;display:flex;align-items:center;gap:16px;font-size:18px;font-weight:700;color:var(--white)}
.finfo .label{color:var(--red)}
.bottom{left:0;top:3043px;width:1200px;height:45px;background:var(--blue)}
.bottom .red{position:absolute;left:0;top:0;width:437px;height:45px;background:var(--red);clip-path:polygon(0 0,92% 0,100% 100%,0 100%)}
.bottom p{position:absolute;left:99px;top:15px;color:var(--white);font-size:11px}
</style>
</head>
<body>

<div class="abs topbar">
  <div class="abs contact">
    <svg width="16" height="16" viewBox="0 0 24 24" fill="none" stroke="#fff" stroke-width="2"><path d="M5 3h4l2 5-2.5 1.5a11 11 0 0 0 6 6L16 13l5 2v4a2 2 0 0 1-2 2A16 16 0 0 1 3 5a2 2 0 0 1 2-2z"/></svg>
    <span>+1 (555) 010-2323 &nbsp;|</span>
    <svg width="17" height="13" viewBox="0 0 24 18" fill="none" stroke="#fff" stroke-width="2"><rect x="1" y="1" width="22" height="16"/><path d="M1 1l11 9 11-9"/></svg>
    <span>info@example.com</span>
  </div>
  <div class="social"><span></span><span></span><span></span></div>
</div>

<div class="abs hero-bg" role="img" aria-label="Climber scaling a sunlit rock face against a hazy sky"></div>
<nav class="abs nav">
  <a class="active">Home</a><a>About Us</a><a>Services</a><a>Members</a><a>Contact Us</a>
</nav>
<div class="wordmark hero-mark"><span class="mark"></span>Norvale Partners</div>
<h1 class="abs hero-title">Lorem Ipsum Is<span class="red">Dummy Text</span></h1>
<p class="abs hero-text">Lorem Ipsum is simply dummy text of the printing and typesetting industry. Lorem Ipsum has been the industry's standard dummy text ever since the 1500s,</p>
<div class="btn" style="left:99px;top:464px;width:122px;height:37px">Contact Us</div>
<div class="abs dots"><span></span><span class="on"></span><span></span></div>

<section>
  <div class="abs frame"></div>
  <div class="photo" style="left:99px;top:627px;width:243px;height:330px;background:linear-gradient(160deg,#2f6fc4 0%,#8fb3dc 45%,#cfd6dc 65%,#6e5e4c 100%)" role="img" aria-label="Hiker with backpack facing a snowy mountain peak"></div>
  <div class="photo" style="left:315px;top:716px;width:243px;height:329px;background:linear-gradient(180deg,#6f6a64 0%,#9a928a 45%,#d9dde3 75%,#eef1f4 100%)" role="img" aria-label="Cross-country skier racing through a birch forest"></div>
  <h2 class="abs heading about-title">About Us</h2>
  <div class="abs tagline about-tag">Lorem Ipsum is simply dummy text of the printing .</div>
  <p class="abs about-text">Lorem Ipsum is simply dummy text of the printing and typesetting industry. Lorem Ipsum has been the industry's standard dummy text ever since the 1500s, when an unknown printer took a galley of type and scrambled it to make a type specimen book. It has survived not only five centuries, but also the leap into electronic typesetting, remaining essentially unchanged. It was popularised in the 1960s with the release of Letraset sheets containing Lorem Ipsum passages, and more recently with desktop publishing software like Aldus PageMaker including versions of Lorem Ipsum.</p>
  <div class="btn" style="left:613px;top:975px;width:121px;height:37px">Read More</div>
</section>

<section>
  <div class="abs services-bg" role="img" aria-label="Snowy glacier slope with distant climbers"></div>
  <h2 class="abs center heading services-title">Our Services</h2>
  <div class="abs center tagline services-tag">Lorem Ipsum is simply dummy text of the printing .</div>
  <div class="svc" style="left:99px;top:1327px"><div class="icon" role="img" aria-label="Leader with flag icon"></div><h3>LOREM IPSUM IS SIMPLY DUMMY TEXT</h3><p>Lorem Ipsum has been the industry's standard dummy text ever since the 1500s... <em>+Read More</em></p></div>
  <div class="svc" style="left:613px;top:1327px"><div class="icon" role="img" aria-label="Team and handshake icon"></div><h3>LOREM IPSUM IS SIMPLY DUMMY TEXT</h3><p>Lorem Ipsum has been the industry's standard dummy text ever since the 1500s... <em>+Read More</em></p></div>
  <div class="svc" style="left:99px;top:1458px"><div class="icon" role="img" aria-label="Award winner icon"></div><h3>LOREM IPSUM IS SIMPLY DUMMY TEXT</h3><p>Lorem Ipsum has been the industry's standard dummy text ever since the 1500s... <em>+Read More</em></p></div>
  <div class="svc" style="left:613px;top:1458px"><div class="icon" role="img" aria-label="Report document icon"></div><h3>LOREM IPSUM IS SIMPLY DUMMY TEXT</h3><p>Lorem Ipsum has been the industry's standard dummy text ever since the 1500s... <em>+Read More</em></p></div>
  <div class="svc" style="left:99px;top:1588px"><div class="icon" role="img" aria-label="Stopwatch icon"></div><h3>LOREM IPSUM IS SIMPLY DUMMY TEXT</h3><p>Lorem Ipsum has been the industry's standard dummy text ever since the 1500s... <em>+Read More</em></p></div>
  <div class="svc" style="left:613px;top:1588px"><div class="icon" role="img" aria-label="Stacked coins icon"></div><h3>LOREM IPSUM IS SIMPLY DUMMY TEXT</h3><p>Lorem Ipsum has been the industry's standard dummy text ever since the 1500s... <em>+Read More</em></p></div>
</section>

<section>
  <h2 class="abs center heading members-title">Our Members</h2>
  <div class="abs center tagline members-tag">Contrary to popular belief, Lorem Ipsum is not simply random text.</div>
  <div class="card" style="left:101px"><div class="pic" role="img" aria-label="Portrait of a team member" style="background:linear-gradient(180deg,#f2f2f2 0%,#d8cfc6 60%,#3a3a3a 100%)"></div><div class="cap"><b>Lorem Ipsum</b><span>It is simply dummy text of the</span></div></div>
  <div class="card" style="left:357px"><div class="pic" role="img" aria-label="Portrait of a team member" style="background:linear-gradient(180deg,#f3f1ee 0%,#e0d1b3 60%,#4a4a4a 100%)"></div><div class="cap"><b>Lorem Ipsum</b><span>It is simply dummy text of the</span></div></div>
  <div class="card" style="left:614px"><div class="pic" role="img" aria-label="Portrait of a team member" style="background:linear-gradient(180deg,#d9ecd9 0%,#d8c2b3 60%,#2c2c2c 100%)"></div><div class="cap"><b>Lorem Ipsum</b><span>It is simply dummy text of the</span></div></div>
  <div class="card" style="left:870px"><div class="pic" role="img" aria-label="Portrait of a team member" style="background:linear-gradient(180deg,#3c3c3c 0%,#8c7a6c 55%,#1e1e1e 100%)"></div><div class="cap"><b>Lorem Ipsum</b><span>It is simply dummy text of the</span></div></div>
</section>

<section>
  <div class="abs contact-bg" role="img" aria-label="Alpine ski racer carving through powder snow"></div>
  <h2 class="abs heading contact-title">Contact Form</h2>
  <div class="abs tagline contact-tag">Contrary to popular belief, Lorem Ipsum is not simply random text.</div>
  <div class="field" style="left:613px;top:2531px;width:230px">Name</div>
  <div class="field" style="left:870px;top:2531px;width:230px">Address</div>
  <div class="field" style="left:613px;top:2593px;width:230px">Email</div>
  <div class="field" style="left:870px;top:2593px;width:230px">Phone</div>
  <div class="field" style="left:613px;top:2656px;width:487px;height:61px">Question/Comment</div>
  <div class="btn" style="left:613px;top:2744px;width:121px;height:37px">Contact Us</div>
</section>

<footer>
  <div class="abs footer-bg" role="img" aria-label="Dark mountain range at night"></div>
  <div class="wordmark foot-mark"><span class="mark"></span>Norvale Partners</div>
  <div class="abs fnav"><span class="active">Home</span><span>About Us</span><span>Services</span><span>Members</span><span>Contact Us</span></div>
  <div class="abs finfo"><span><span class="label">Contact Info:</span> +000-000-0000</span><div class="social"><span></span><span></span><span></span></div></div>
  <div class="abs bottom"><div class="red"></div><p>©2019 by Norvale Partners. All rights reserved.</p></div>
</footer>

</body>
</html>
```